Design Home Screen

We’re looking for talented UI/UX designers to create an eye-popping, modern, and fun Home Screen for the Quenzo app — the future of real-time earned wage access and financial empowerment.
Your mission: make the Quenzo experience come alive the moment users open the app.

Design Goals

The screen should instantly communicate energy, financial control, and trust.

The “Time on the Clock” and the “Quenzo Balance” must be the stars of the screen — presented in a way that feels alive, interactive, and rewarding.

Think of how to visually celebrate a user’s progress at work and their earnings — something that makes checking the app feel fun and satisfying, not transactional.

Creative Direction

Style: Sleek, fintech-modern, with motion or visual elements that feel alive (micro-animations, glowing accents, gradient depth, or movement cues).

Tone: Confident, vibrant, and optimistic — this is a financial app that feels human and inspiring.

Color palette: Black, Gold, and Green, and any other color.

Typography: Clean, readable, and balanced between playful and professional.

Must-Have Elements

Time on the Clock – creatively displayed (e.g., countdown or progress animation as the user works).

Quenzo Balance – bold, fun, and maybe even interactive (reflecting growth as the user earns).

A clean navigation structure for core tabs: Home, Access Pay, Boost, History, Profile.

Engaging micro-animations, icons, or progress indicators that make the user feel “in motion.”

Room for brand personality — the “Quenzo” name and logo if desired.

```html
<!DOCTYPE html>
<html lang="en">
<head>
<meta charset="utf-8">
<title>Quenzo – Home</title>
<link href="https://fonts.googleapis.com/css2?family=Poppins:wght@400;500;600;700&display=swap" rel="stylesheet">
<style>
:root{
  --bg:#000;
  --gold:#e5b84a;
  --gold-deep:#b8913a;
  --green:#3fa36b;
  --green-bright:#2fbf5a;
  --ring:#2c3a2c;
  --text:#fff;
  --muted:#8d8d8d;
  --card-gold:#1e1a10;
  --card-green:#111a14;
  --nav:#1c1c1c;
}
*{margin:0;padding:0;box-sizing:border-box}
html,body{width:1200px;height:4080px;overflow:hidden;background:var(--bg)}
body{font-family:'Poppins',sans-serif;color:var(--text);position:relative}
.abs{position:absolute}
.status-time{left:86px;top:50px;font-size:45px;font-weight:600}
.status-icons{right:34px;top:54px}
.avatar{left:64px;top:173px;width:160px;height:160px;border-radius:50%;background:radial-gradient(circle at 50% 40%,#6b5448,#2e2622 70%,#d9d9d9 71%)}
.welcome{left:275px;top:186px;font-size:38px;color:#9a9a9a}
.user-name{left:275px;top:252px;font-size:60px;font-weight:500}
.bell{left:1002px;top:186px;width:134px;height:134px;border-radius:50%;background:linear-gradient(135deg,#e3b94b,#9c7a2a);display:flex;align-items:center;justify-content:center}
.clock-title{left:0;width:1200px;top:444px;text-align:center;font-size:42px;color:var(--gold);font-weight:500}
.clock{left:200px;top:549px}
.work-row{left:69px;right:67px;top:1460px;display:flex;align-items:center;font-size:42px}
.work-row .label{font-weight:500;flex:1}
.work-row .hrs{color:var(--gold)}
.work-row .sep{width:3px;height:78px;background:#444;transform:rotate(12deg);margin:0 24px}
.work-row .rate{color:var(--green);font-weight:500}
.rule{left:0;width:1200px;height:3px;background:var(--gold-deep)}
.balance-label{left:0;width:1200px;top:1658px;text-align:center;font-size:42px;font-weight:500}
.balance{left:0;width:1200px;top:1720px;text-align:center;font-size:166px;font-weight:700;color:var(--gold);letter-spacing:2px;line-height:1.2}
.period{left:131px;right:131px;top:1970px;display:flex;justify-content:space-between;font-size:42px;font-weight:500}
.period .date{color:var(--gold)}
.period .date small{font-size:38px;margin-right:14px}
.actions{left:0;width:1200px;top:2177px}
.action{position:absolute;width:300px;margin-left:-150px;text-align:center}
.action .ring{width:170px;height:170px;border-radius:50%;margin:0 auto;display:flex;align-items:center;justify-content:center;border:3px solid var(--gold-deep)}
.action .ring.green{border-color:var(--green);background:#12201a}
.action .name{font-size:42px;line-height:48px;margin-top:40px}
.divider{left:70px;width:1066px;top:2555px;height:2px;background:#1e1e1e}
.tx-title{left:66px;top:2615px;font-size:58px;font-weight:500}
.see-all{right:64px;top:2628px;font-size:45px;color:var(--gold);font-weight:500}
.card{left:19px;width:1159px;height:230px;border-radius:32px;border:3px solid var(--gold-deep);background:var(--card-gold)}
.card.green{border-color:var(--green);background:var(--card-green)}
.card .logo{position:absolute;left:47px;top:45px;width:134px;height:134px;border-radius:50%}
.card .who{position:absolute;left:234px;top:44px}
.card .who b{display:block;font-size:51px;font-weight:500}
.card .who span{font-size:38px;color:var(--muted)}
.card .amt{position:absolute;right:292px;top:78px;font-size:51px;font-weight:500}
.card .st{position:absolute;right:40px;top:66px;text-align:right;line-height:44px}
.card .st b{display:block;font-size:38px;font-weight:500;color:var(--green-bright)}
.card .st b.pending{color:var(--gold)}
.card .st span{font-size:35px}
.nav{left:0;width:1200px;top:3805px;height:275px;background:var(--nav);border-radius:0 0 60px 60px}
.tab{position:absolute;top:58px;width:240px;margin-left:-120px;text-align:center;color:#9a9a9a;font-size:35px}
.tab svg{display:block;margin:0 auto 14px}
.tab.active{color:var(--gold)}
</style>
</head>
<body>
<div class="abs status-time">9:41</div>
<svg class="abs status-icons" width="210" height="44" viewBox="0 0 210 44">
  <g fill="#fff"><rect x="0" y="28" width="8" height="10" rx="2"/><rect x="13" y="22" width="8" height="16" rx="2"/><rect x="26" y="15" width="8" height="23" rx="2"/><rect x="39" y="8" width="8" height="30" rx="2"/></g>
  <path d="M70 16a30 30 0 0 1 42 0M77 23a20 20 0 0 1 28 0M84 30a10 10 0 0 1 14 0" stroke="#fff" stroke-width="5" fill="none" stroke-linecap="round"/>
  <rect x="130" y="6" width="70" height="32" rx="9" fill="none" stroke="#fff" stroke-width="3"/>
  <rect x="135" y="11" width="60" height="22" rx="5" fill="#fff"/>
</svg>

<div class="abs avatar" role="img" aria-label="User profile photo"></div>
<div class="abs welcome">Welcome back,</div>
<div class="abs user-name">Maren Okafor</div>
<div class="abs bell">
  <svg width="72" height="72" viewBox="0 0 24 24" fill="none" stroke="#fff" stroke-width="1.6" stroke-linecap="round" stroke-linejoin="round"><path d="M6 16V11a6 6 0 0 1 12 0v5l1.5 2h-15z"/><path d="M10 20.5a2 2 0 0 0 4 0"/><path d="M12 3v2"/></svg>
</div>

<div class="abs clock-title">Status On the Clock</div>
<svg class="abs clock" width="800" height="800" viewBox="0 0 800 800">
  <defs>
    <linearGradient id="arcGrad" x1="0" y1="0" x2="1" y2="1">
      <stop offset="0" stop-color="#b08c3a"/><stop offset="1" stop-color="#f0c24c"/>
    </linearGradient>
  </defs>
  <circle cx="400" cy="400" r="380" fill="none" stroke="var(--gold-deep)" stroke-width="6" stroke-dasharray="2 37.79" transform="rotate(-90 400 400)"/>
  <circle cx="400" cy="400" r="385" fill="none" stroke="var(--gold)" stroke-width="28" stroke-dasharray="3 198.59" stroke-dashoffset="1.5" transform="rotate(-90 400 400)"/>
  <circle cx="400" cy="400" r="323" fill="none" stroke="var(--ring)" stroke-width="58"/>
  <circle cx="400" cy="400" r="323" fill="none" stroke="url(#arcGrad)" stroke-width="58" stroke-linecap="round" stroke-dasharray="600 2100" transform="rotate(-86 400 400)"/>
  <line x1="384" y1="454" x2="384" y2="235" stroke="#fff" stroke-width="13" stroke-linecap="round"/>
  <line x1="356" y1="467" x2="520" y2="531" stroke="#fff" stroke-width="11" stroke-linecap="round"/>
  <line x1="356" y1="470" x2="632" y2="360" stroke="var(--gold)" stroke-width="9" stroke-linecap="round"/>
  <circle cx="384" cy="454" r="15" fill="var(--gold)"/>
</svg>

<div class="abs work-row">
  <span class="label">Work Hours:</span>
  <span class="hrs">15:00 HRS.</span><span class="sep"></span><span class="rate">@$20.00/hr</span>
</div>

<div class="abs rule" style="top:1590px"></div>
<div class="abs balance-label">Quenzo Wage Balance:</div>
<div class="abs balance">$12,450</div>
<div class="abs period"><span>Current Pay Period:</span><span class="date"><small>JUNE</small>01/06/2025</span></div>
<div class="abs rule" style="top:2091px"></div>

<div class="abs actions">
  <div class="action" style="left:154px">
    <div class="ring"><svg width="76" height="76" viewBox="0 0 24 24" fill="none" stroke="var(--gold)" stroke-width="1.6" stroke-linecap="round" stroke-linejoin="round"><path d="M12 5v10M8 11l4 4 4-4M6 19h12"/></svg></div>
    <div class="name">Request<br>Money</div>
  </div>
  <div class="action" style="left:451px">
    <div class="ring green"><svg width="76" height="76" viewBox="0 0 24 24" fill="none" stroke="#fff" stroke-width="1.6" stroke-linecap="round" stroke-linejoin="round"><path d="M19 11a7 7 0 1 1-6-6.9"/><path d="M20 4l-4 4M16 5v3h3"/><path d="M13.5 9.5c-.5-.6-1.2-.8-2-.8-1 0-1.8.6-1.8 1.4 0 1.8 4 1 4 3 0 .8-.9 1.4-2 1.4-.9 0-1.7-.3-2.2-.9M11.5 7.5v1.2M11.5 14.5v1.2"/></svg></div>
    <div class="name">Loan<br>Access</div>
  </div>
  <div class="action" style="left:749px">
    <div class="ring"><svg width="76" height="76" viewBox="0 0 24 24" fill="none" stroke="var(--gold)" stroke-width="1.6" stroke-linecap="round"><circle cx="12" cy="12" r="8"/><path d="M12 8v8M8 12h8"/></svg></div>
    <div class="name">Update<br>Employment</div>
  </div>
  <div class="action" style="left:1050px">
    <div class="ring green"><svg width="76" height="76" viewBox="0 0 24 24" fill="none" stroke="#fff" stroke-width="1.6" stroke-linejoin="round"><path d="M5 7h11a3 3 0 0 1 3 3v7a2 2 0 0 1-2 2H6a2 2 0 0 1-2-2V8a2 2 0 0 1 2-2h9"/><path d="M19 11h-3a1.5 1.5 0 0 0 0 3h3z"/></svg></div>
    <div class="name">Earn<br>$10,000</div>
  </div>
</div>

<div class="abs divider"></div>
<div class="abs tx-title">Transaction</div>
<div class="abs see-all">See All</div>

<div class="abs card" style="top:2734px">
  <div class="logo" role="img" aria-label="Contact portrait" style="background:linear-gradient(#d7dde2,#9aa6ae)"></div>
  <div class="who"><b>Jon Dale Inc.</b><span>Sep 10, 2025</span></div>
  <div class="amt">$5,99</div>
  <div class="st"><b>Sent</b><span>Payvia</span></div>
</div>
<div class="abs card green" style="top:2996px">
  <div class="logo" role="img" aria-label="Verano Inc. emblem" style="background:#0e0e0e"></div>
  <div class="who"><b>Verano Inc.</b><span>June 19, 2025</span></div>
  <div class="amt">$12,99</div>
  <div class="st"><b>Sent</b><span>Payvia</span></div>
</div>
<div class="abs card" style="top:3258px">
  <div class="logo" role="img" aria-label="Taskly emblem" style="background:#14a800"></div>
  <div class="who"><b>Taskly</b><span>Sep 10, 2025</span></div>
  <div class="amt">$300</div>
  <div class="st"><b class="pending">Pending</b><span>Payvia</span></div>
</div>
<div class="abs card green" style="top:3520px">
  <div class="logo" role="img" aria-label="Petal Deals emblem" style="background:#f4f4f4"></div>
  <div class="who"><b>Petal Deals</b><span>June 19, 2025</span></div>
  <div class="amt">$88</div>
  <div class="st"><b>Sent</b><span>Payvia</span></div>
</div>

<nav class="abs nav">
  <div class="tab active" style="left:120px">
    <svg width="70" height="70" viewBox="0 0 24 24" fill="none" stroke="var(--gold)" stroke-width="1.6" stroke-linejoin="round"><path d="M4 10.5 12 4l8 6.5V18a2 2 0 0 1-2 2H6a2 2 0 0 1-2-2z"/><path d="M9 15h6" stroke-linecap="round"/></svg>Home
  </div>
  <div class="tab" style="left:360px">
    <svg width="70" height="70" viewBox="0 0 24 24" fill="none" stroke="#9a9a9a" stroke-width="1.6" stroke-linecap="round"><rect x="3.5" y="5" width="17" height="14" rx="2"/><path d="M3.5 10h17M7 15h2M11 15h2"/></svg>Access Pay
  </div>
  <div class="tab" style="left:600px">
    <svg width="70" height="70" viewBox="0 0 24 24" fill="none" stroke="#9a9a9a" stroke-width="1.6" stroke-linecap="round" stroke-linejoin="round"><path d="M6 18 17 7M10 7h7v7M6 13l5-5"/></svg>Boost
  </div>
  <div class="tab" style="left:840px">
    <svg width="70" height="70" viewBox="0 0 24 24" fill="none" stroke="#9a9a9a" stroke-width="1.6" stroke-linecap="round" stroke-linejoin="round"><path d="M4 12a8 8 0 1 0 2.3-5.7M4 4v4h4"/><path d="M12 8v4l3 2"/></svg>History
  </div>
  <div class="tab" style="left:1080px">
    <svg width="70" height="70" viewBox="0 0 24 24" fill="none" stroke="#9a9a9a" stroke-width="1.6" stroke-linecap="round"><circle cx="12" cy="8" r="4"/><path d="M4.5 20a7.5 7.5 0 0 1 15 0"/></svg>Profile
  </div>
</nav>
</body>
</html>
```